Business card design needed

We are a wine business involved in winemaking, broking and packaging on behalf of clients globally with the majority being Asian. The design should be quite traditional and classic with some red used, font used should be easily read.

Target Market(s)

Trade customers other business owners

Industry/Entity Type

Business

Contact Information for Business Card

Rosalind Thwaite
Meridale Wine Collective
PO Box 738, Fenwick Vale
South Australia 5187
Phone: +61 (0)455 982 317
Email: kvcellars@brightmail.example

Logo styles of interest
Lettermark Logo

```html
<!DOCTYPE html>
<html lang="en">
<head>
<meta charset="utf-8">
<title>Meridale Wine Collective — Business Card</title>
<link href="https://fonts.googleapis.com/css2?family=Archivo+Narrow:wght@500&family=Open+Sans:wght@400&family=Marcellus+SC&display=swap" rel="stylesheet">
<style>
  :root {
    --wine-red: #bd1f2d;
    --charcoal: #3f3f42;
    --stripe-grey: #4a4a4c;
    --paper: #ffffff;
    --ink: #1d1d1d;
    --backdrop: #262626;
    --glass-tone: #e9d9cf;
  }
  * { margin: 0; padding: 0; box-sizing: border-box; }
  html, body {
    width: 1200px; height: 1200px; overflow: hidden;
    background: var(--backdrop);
  }
  .sheet {
    position: relative; width: 1200px; height: 1200px;
    display: flex; flex-direction: column; align-items: center;
    justify-content: center; gap: 80px;
  }
  .card {
    position: relative; width: 900px; height: 500px; overflow: hidden;
    box-shadow: 0 18px 40px rgba(0,0,0,0.55);
  }

  /* Contact side */
  .card--contact {
    background: var(--paper);
    border: 12px solid var(--wine-red);
  }
  .glass-photo {
    position: absolute; right: 40px; top: 30px; width: 300px; height: 330px;
    border-radius: 50% 50% 40% 40%;
    background: radial-gradient(ellipse at 50% 40%, var(--glass-tone) 0%, rgba(233,217,207,0.35) 55%, rgba(255,255,255,0) 75%);
  }
  .contact-title {
    position: absolute; left: 40px; top: 42px;
    font-family: "Archivo Narrow", sans-serif; font-weight: 500;
    font-size: 46px; color: var(--wine-red); letter-spacing: -0.5px;
  }
  .contact-address {
    position: absolute; left: 96px; top: 120px;
    font-family: "Open Sans", sans-serif; font-size: 25px; color: var(--ink);
  }
  .contact-lines {
    position: absolute; left: 330px; top: 200px;
    display: flex; flex-direction: column; gap: 20px;
    font-family: "Open Sans", sans-serif; font-size: 25px; color: var(--ink);
  }
  .contact-line { display: flex; align-items: center; gap: 18px; }
  .contact-icon { width: 34px; height: 28px; flex: none; }
  .contact-footer { position: absolute; left: 0; bottom: 0; width: 876px; height: 110px; }
  .footer-tag {
    position: absolute; right: 14px; bottom: 20px;
    font-family: "Archivo Narrow", sans-serif; font-size: 17px; color: var(--paper);
  }

  /* Brand side */
  .card--brand { background: var(--charcoal); }
  .brand-shapes { position: absolute; inset: 0; }
  .brand-name {
    position: absolute; left: 60px; top: 48px;
    font-family: "Marcellus SC", serif; color: var(--paper);
    font-size: 58px; line-height: 1.2; letter-spacing: 5px;
  }
  .brand-name span { display: block; }
  .brand-name .line-2 { padding-left: 60px; }
  .brand-name .line-3 { padding-left: 420px; }
</style>
</head>
<body>
<main class="sheet">

  <section class="card card--contact">
    <div class="glass-photo" role="img" aria-label="Soft photograph of a glass of white wine"></div>
    <h1 class="contact-title">Rosalind Thwaite Meridale Wine Collective</h1>
    <p class="contact-address">PO Box 738, Fenwick Vale South Australia 5187</p>
    <div class="contact-lines">
      <p class="contact-line">
        <svg class="contact-icon" viewBox="0 0 34 28" aria-hidden="true">
          <rect width="34" height="28" rx="5" fill="var(--wine-red)"/>
          <path d="M11 7c-2 1-2 4 0 8s6 7 9 7c2 0 3-1 3-2l-3-3-2 1c-2-1-4-3-5-5l1-2-3-4z" fill="#fff"/>
        </svg>
        +61 (0)455 982 317
      </p>
      <p class="contact-line">
        <svg class="contact-icon" viewBox="0 0 34 28" aria-hidden="true">
          <rect x="2" y="4" width="30" height="20" fill="var(--wine-red)"/>
          <path d="M3 5l14 11L31 5" fill="none" stroke="#fff" stroke-width="2"/>
        </svg>
        kvcellars@brightmail.example
      </p>
    </div>
    <svg class="contact-footer" viewBox="0 0 876 110" aria-hidden="true">
      <polygon points="0,96 540,96 560,62 876,62 876,110 0,110" fill="var(--wine-red)"/>
      <polygon points="0,82 545,82 565,48 600,48 576,90 0,90" fill="var(--stripe-grey)"/>
    </svg>
    <p class="footer-tag">Rosalind Thwaite Meridale Wine Collective</p>
  </section>

  <section class="card card--brand">
    <svg class="brand-shapes" viewBox="0 0 900 500" aria-hidden="true">
      <polygon points="400,218 860,218 860,400 0,400 0,300 400,300" fill="var(--wine-red)"/>
      <rect x="860" y="0" width="22" height="500" fill="var(--paper)"/>
      <circle cx="190" cy="350" r="92" fill="var(--wine-red)" stroke="var(--paper)" stroke-width="18"/>
    </svg>
    <h2 class="brand-name">
      <span class="line-1">Rosalind Thwaite</span>
      <span class="line-2">Meridale Wine</span>
      <span class="line-3">Collective</span>
    </h2>
  </section>

</main>
</body>
</html>
```